Research Flier

I need to take a very bad flier that I made and turn it into an amazing flyer for my research group to be shared at a high profile conference.

```html
<!DOCTYPE html>
<html lang="en">
<head>
<meta charset="utf-8">
<title>The Kindred Lab – Research Flier</title>
<link href="https://fonts.googleapis.com/css2?family=Poppins:wght@300;400;500;600;700;800&family=Roboto:wght@700;900&display=swap" rel="stylesheet">
<style>
:root{
  --blue:#0a6bbf;
  --blue-dark:#0759a3;
  --green:#a4d05f;
  --red:#d9432a;
  --grey-band:#ececec;
  --ink:#111;
  --white:#fff;
  --stage:#d9d9d9;
}
*{box-sizing:border-box;margin:0;padding:0}
html,body{width:1200px;height:1117px;overflow:hidden}
body{background:var(--stage);font-family:"Poppins",sans-serif;color:var(--ink);position:relative}
.page{position:absolute;top:165px;width:557px;height:786px;background:var(--white);overflow:hidden}
.page--front{left:30px}
.page--back{left:613px}
.page-header{position:absolute;top:0;left:0;width:557px;height:55px}
.page-title{position:absolute;top:6px;left:0;width:557px;text-align:center;color:var(--white);font-weight:800}
.page--front .page-title{font-size:24px;letter-spacing:.3px}
.page--back .page-title{font-size:16.5px;top:14px;letter-spacing:.2px}
.pill{position:absolute;color:var(--white);text-align:center;border-radius:4px;font-family:"Roboto",sans-serif;font-weight:900}
.pill--red{background:var(--red)}
.pill--blue{background:var(--blue)}
.pill--green{background:var(--green);color:var(--ink)}

/* front */
.mission-band{position:absolute;top:73px;left:0;width:557px;height:159px;background:var(--grey-band)}
.mission-list{position:absolute;top:92px;left:44px;width:480px;list-style:none;font-size:9.4px;line-height:12.6px}
.mission-list li{position:relative;padding-left:13px;margin-bottom:12px}
.mission-list li::before{content:"";position:absolute;left:0;top:5px;width:3px;height:3px;border-radius:50%;background:var(--blue)}
.rule{position:absolute;height:2px}
.sites-intro{position:absolute;top:277px;left:0;width:557px;text-align:center;font-size:9.4px;line-height:11.8px}
.sites-map{position:absolute;top:303px;left:40px;width:478px;height:64px;background:linear-gradient(90deg,#f3e3e1,#f1f1f1 40%,#f4e6e4 70%,#f1f1f1)}
.sites-table{position:absolute;top:306px;left:46px;width:470px;display:flex;gap:4px}
.site{flex:1}
.site h4{font-size:6px;font-weight:700;line-height:7px;margin-bottom:2px}
.site p{font-size:3.4px;line-height:4.3px;color:#333}
.change-sub{position:absolute;top:419px;left:42px;font-size:10.3px;font-weight:700;color:var(--blue)}
.change-list{position:absolute;top:436px;left:42px;width:222px;list-style:none;font-size:9.2px;line-height:11px}
.change-list li{position:relative;padding-left:12px;margin-bottom:11px}
.change-list li::before{content:"";position:absolute;left:0;top:4px;width:3px;height:3px;border-radius:50%;background:var(--blue)}
.photo{position:absolute;top:557px;left:0;width:278px;height:210px;background:linear-gradient(120deg,#c9d6e3,#e9eef3 45%,#b9a48f 75%,#5e4a3e)}
.domains{position:absolute;top:378px;left:278px;width:279px;height:389px;background:var(--blue);border-top-left-radius:46px;color:var(--white)}
.domain{position:absolute;width:104px;text-align:center}
.domain svg{display:block;margin:0 auto 4px}
.domain h5{font-size:8px;font-weight:600;line-height:10px;white-space:nowrap;margin:0 -10px}
.domain p{font-size:6.9px;font-weight:300;line-height:8.6px}
.voice{position:absolute;left:15px;top:276px;display:flex;gap:10px;align-items:flex-start;width:245px}
.voice h5{font-size:8px;font-weight:600;line-height:10px}
.voice p{font-size:6.9px;font-weight:300;line-height:8.6px}
.footer-shape{position:absolute;left:0;top:700px;width:557px;height:86px}
.partner{position:absolute;display:flex;align-items:center;gap:6px}
.partner-dot{border-radius:50%;background:var(--blue);flex:none}
.center-name{font-size:6.8px;line-height:8.4px;color:#444}
.uni-name{position:absolute;font-size:8.4px;font-weight:500;letter-spacing:.4px;color:#222}
.brand-name{font-weight:600;color:#333;white-space:nowrap}
.badge{flex:none}
.site-url{position:absolute;font-size:6px;color:#1b3fa6;text-decoration:underline}

/* back */
.cards{position:absolute;top:58px;left:42px;display:flex;gap:8px}
.card{width:152px;height:182px;border:2px solid var(--green);border-radius:9px;padding:8px 10px 10px 15px;box-shadow:3px 4px 0 #d6d6d6;display:flex;flex-direction:column;background:var(--white)}
.card h3{font-size:9.3px;font-weight:700;color:var(--red);line-height:10.6px;margin-bottom:2px}
.card p{font-size:9.3px;line-height:12.4px}
.card-visual{margin-top:auto;height:70px;border-radius:4px}
.card-visual--screens{background:linear-gradient(135deg,#f6dcc8,#eceff4 60%,#d9d9d9)}
.card-visual--chart{height:50px;background:linear-gradient(180deg,#eef2f7,#d4dbe4)}
.key-areas{position:absolute;top:290px;left:42px;width:480px;font-size:9.3px;line-height:13px}
.key-areas p{margin-bottom:12px}
.key-areas b{font-weight:700}
.team-band{position:absolute;top:362px;left:0;width:557px;height:90px;background:var(--grey-band)}
.team-title{position:absolute;top:369px;left:0;width:557px;text-align:center;font-size:15.5px;line-height:20px;font-weight:800;color:var(--blue)}
.team-note{position:absolute;top:390px;left:40px;width:477px;text-align:center;font-size:9.4px;font-weight:600;line-height:12.5px}
.team-panel{position:absolute;top:440px;left:16px;width:527px;height:330px;background:var(--blue);border-radius:36px 36px 0 0;box-shadow:0 0 0 4px var(--white)}
.pubs{position:absolute;top:459px;left:34px;width:490px;text-align:center;color:var(--white);font-size:6.6px;font-weight:600;line-height:8.7px}
.pubs p{margin-bottom:9.6px}
</style>
</head>
<body>

<section class="page page--front" aria-label="Front page">
  <svg class="page-header" viewBox="0 0 557 55" aria-hidden="true">
    <rect x="0" y="0" width="557" height="8" fill="#0a6bbf"/>
    <path d="M0 19 H104 q6 0 8 4 l2 4 H0Z" fill="#a4d05f"/>
    <path d="M557 19 H453 q-6 0 -8 4 l-2 4 H557Z" fill="#a4d05f"/>
    <path d="M100 0 C118 0 118 50 142 50 L415 50 C439 50 439 0 457 0Z" fill="#0a6bbf"/>
  </svg>
  <h1 class="page-title">THE KINDRED LAB</h1>

  <div class="mission-band"></div>
  <div class="pill pill--red" style="top:62px;left:182px;width:192px;height:21px;font-size:14px;line-height:22px">MISSION</div>
  <ul class="mission-list">
    <li>Supporting the development of the evidence-based, HEART Learning program and KBT for Educators by assessing program implementation and examining feasibility, impact, and long-term sustainability at the school, district, city, and national levels.</li>
    <li>Developing effective tools and measures to KBT and HEART Learning</li>
    <li>Support global dissemination through impactful manualization</li>
    <li>Contribute to compassion-based education studies worldwide through scientific advancements that examine compassion, common humanity, wellbeing, interdependence, and secular ethics.</li>
  </ul>

  <div class="rule" style="top:252px;left:43px;width:473px;background:var(--blue)"></div>
  <div class="pill pill--blue" style="top:242px;left:182px;width:192px;height:22px;font-size:14px;line-height:22px">RESEARCH SITES</div>
  <p class="sites-intro">We collaborate with global affiliates to conduct collaborative region-specific research.<br>Read below to discover the impactful projects from our worldwide network!</p>
  <div class="sites-map" role="img" aria-label="Faint world map showing the research site countries"></div>
  <div class="sites-table">
    <div class="site"><h4>USA</h4><p>Multiple elementary studies; RCT and mixed methods</p></div>
    <div class="site"><h4>Sweden</h4><p>Late elementary; 2 schools; feasibility study</p></div>
    <div class="site"><h4>Spain</h4><p>Multiple schools; two regions; pilot study</p></div>
    <div class="site"><h4>Ukraine</h4><p>Teachers; feasibility and impact study</p></div>
    <div class="site"><h4>Mongolia</h4><p>High school; 800+ students; 5 schools</p></div>
    <div class="site"><h4>Mexico</h4><p>Pre-service course; pilot study</p></div>
    <div class="site"><h4>Columbia</h4><p>300+ students; implementation study</p></div>
    <div class="site"><h4>Brazil</h4><p>Ten schools; controlled trial</p></div>
    <div class="site"><h4>Kenya</h4><p>2 schools; feasibility study</p></div>
    <div class="site"><h4>India</h4><p>1300+ students; urban and rural</p></div>
    <div class="site"><h4>South Korea</h4><p>Elementary implementation study</p></div>
  </div>

  <div class="pill pill--green" style="top:388px;left:43px;width:221px;height:23px;font-size:14px;line-height:24px;border-radius:2px">BUILDING FOR CHANGE</div>
  <p class="change-sub">To meaningfully impact change, we have:</p>
  <ul class="change-list">
    <li>Identified seven critical domains for whole-school implementation sustainment</li>
    <li>Conducted studies on sustainable implementation and its impact on compassionate systems</li>
    <li>Begun work on global implementation frameworks, monitoring guides, and whole-school trainings</li>
  </ul>

  <div class="photo" role="img" aria-label="Photo of two colleagues talking in a bright office"></div>

  <div class="domains">
    <div class="domain" style="left:8px;top:15px">
      <svg width="32" height="32" viewBox="0 0 32 32" fill="#fff" aria-hidden="true"><circle cx="16" cy="9" r="7" fill="none" stroke="#fff" stroke-width="2"/><path d="M16 4l4 5h-3v4h-2V9h-3z"/><circle cx="9" cy="22" r="3"/><circle cx="16" cy="21" r="3"/><circle cx="23" cy="22" r="3"/><path d="M4 32c0-4 2-6 5-6s5 2 5 6zM11 32c0-5 2-7 5-7s5 2 5 7zM18 32c0-4 2-6 5-6s5 2 5 6z"/></svg>
      <h5>Leadership Development</h5>
      <p>Those in leadership need skill and HEART understanding for implementation to thrive.</p>
    </div>
    <div class="domain" style="left:119px;top:15px">
      <svg width="32" height="32" viewBox="0 0 32 32" aria-hidden="true"><rect x="9" y="3" width="18" height="24" fill="none" stroke="#fff" stroke-width="2"/><rect x="5" y="7" width="18" height="24" fill="#0a6bbf" stroke="#fff" stroke-width="2"/><circle cx="14" cy="19" r="5" fill="none" stroke="#fff" stroke-width="2.5" stroke-dasharray="2.5 1.5"/><circle cx="14" cy="19" r="2" fill="#fff"/></svg>
      <h5>Implementation</h5>
      <p>involves strategies that embed SEL into the educational landscape of the school</p>
    </div>
    <div class="domain" style="left:8px;top:98px">
      <svg width="30" height="30" viewBox="0 0 30 30" fill="#fff" aria-hidden="true"><path d="M15 6a7 7 0 0 0-4 12.7V22h8v-3.3A7 7 0 0 0 15 6z"/><rect x="11" y="23" width="8" height="2"/><rect x="12" y="26" width="6" height="2"/><path d="M15 0v3M3 12H0M30 12h-3M5 3l2 2M25 3l-2 2" stroke="#fff" stroke-width="1.6"/></svg>
      <h5>District Initiative Alignment</h5>
      <p>HEART must align with school initiatives as a part of shared goals that are communicated.</p>
    </div>
    <div class="domain" style="left:119px;top:98px">
      <svg width="30" height="30" viewBox="0 0 30 30" fill="#fff" aria-hidden="true"><circle cx="15" cy="6" r="3.5"/><rect x="11" y="11" width="8" height="12" rx="2"/><circle cx="6" cy="9" r="3"/><rect x="2.5" y="13" width="7" height="10" rx="2"/><circle cx="24" cy="9" r="3"/><rect x="20.5" y="13" width="7" height="10" rx="2"/></svg>
      <h5>Adult SEL</h5>
      <p>Professional development includes SEL for adults to create supportive schools.</p>
    </div>
    <div class="domain" style="left:8px;top:178px">
      <svg width="32" height="32" viewBox="0 0 32 32" fill="#fff" aria-hidden="true"><circle cx="9" cy="5" r="2.5"/><circle cx="16" cy="4" r="2.5"/><circle cx="23" cy="5" r="2.5"/><path d="M5 13c0-3 2-5 4-5s4 2 4 5zM12 12c0-3 2-5 4-5s4 2 4 5zM19 13c0-3 2-5 4-5s4 2 4 5z"/><path d="M2 20l6-3 6 3 4-2 6 2 6 0-5 7-6 1-7-3-5 1z"/></svg>
      <h5>Community Engagement</h5>
      <p>Engaging families and communities creates a shared vision that enhances sustainability.</p>
    </div>
    <div class="domain" style="left:119px;top:178px">
      <svg width="32" height="32" viewBox="0 0 32 32" fill="none" stroke="#fff" stroke-width="1.8" aria-hidden="true"><circle cx="16" cy="16" r="4"/><circle cx="5" cy="5" r="3"/><circle cx="27" cy="6" r="3"/><circle cx="5" cy="26" r="3"/><circle cx="27" cy="26" r="3"/><path d="M8 8l5 5M24 9l-5 4M8 23l5-4M24 23l-5-4"/></svg>
      <h5>Communities of Practice</h5>
      <p>Ongoing professional development creates opportunities and spaces to strengthen educator development.</p>
    </div>
    <div class="voice">
      <svg width="38" height="30" viewBox="0 0 38 30" aria-hidden="true"><path d="M2 10h7l9-8v26l-9-8H2z" fill="#fff"/><path d="M23 9q4 6 0 12M28 5q7 10 0 20M33 2q9 13 0 26" fill="none" stroke="#fff" stroke-width="2.6" stroke-linecap="round"/></svg>
      <div>
        <h5>Student Voice</h5>
        <p>Empowering students to actively participate in and contribute to the SEL process strengthens the school community and supports SEL sustainability</p>
      </div>
    </div>
  </div>

  <svg class="footer-shape" viewBox="0 0 557 86" aria-hidden="true">
    <path d="M0 86 V65 H62 C96 65 100 7 142 7 L474 7 C512 7 518 65 557 65 V86Z" fill="#fff"/>
  </svg>
  <div class="partner" style="left:115px;top:718px">
    <span class="partner-dot" style="width:26px;height:26px"></span>
    <span class="center-name">Center for<br>Reflective Science and<br>Care-Based Ethics</span>
  </div>
  <p class="uni-name" style="left:147px;top:751px">HALDEN UNIVERSITY</p>
  <div class="partner" style="left:305px;top:724px">
    <span class="brand-name" style="font-size:14px;line-height:18px">HEART Learning</span>
    <span class="badge" style="width:20px;height:20px;border-radius:50%;margin-left:10px;background:#c9c9c9"></span>
  </div>
  <p class="site-url" style="left:323px;top:753px">https://labs.halden.edu/kindredlab</p>
</section>

<section class="page page--back" aria-label="Back page">
  <svg class="page-header" viewBox="0 0 557 55" aria-hidden="true">
    <rect x="0" y="0" width="557" height="8" fill="#0a6bbf"/>
    <path d="M0 19 H104 q6 0 8 4 l2 4 H0Z" fill="#a4d05f"/>
    <path d="M557 19 H453 q-6 0 -8 4 l-2 4 H557Z" fill="#a4d05f"/>
    <path d="M100 0 C118 0 118 50 142 50 L415 50 C439 50 439 0 457 0Z" fill="#0a6bbf"/>
  </svg>
  <h1 class="page-title">Assessment Development Projects</h1>

  <div class="cards">
    <article class="card">
      <h3>Digital Assessment: HEART Learning Insight</h3>
      <p>curriculum-based assessment tool being developed in collaboration with Tavora</p>
      <div class="card-visual card-visual--screens" role="img" aria-label="Two tablet screens showing the digital assessment app"></div>
    </article>
    <article class="card">
      <h3>Developmentally Appropriate Expectations of Change:</h3>
      <p>We are building age-appropriate rubrics that span the K-12 curriculum. They will help teachers understand expected changes in behavior, communication, relationships, and learning.</p>
    </article>
    <article class="card">
      <h3>Assessment Package for Framework-Based Effectiveness:</h3>
      <p>With affiliates, development of an assessment package for effectiveness studies aimed at assessing domain components, specific to our programs.</p>
      <div class="card-visual card-visual--chart" role="img" aria-label="Grid of domain component icons for the assessment package"></div>
    </article>
  </div>

  <div class="rule" style="top:268px;left:42px;width:474px;background:var(--red)"></div>
  <div class="pill pill--red" style="top:256px;left:131px;width:296px;height:25px;font-family:'Poppins',sans-serif;font-weight:700;font-size:15px;line-height:25px">Other Key Areas of Development</div>
  <div class="key-areas">
    <p><b>Global Implementation Framework:</b> Establishing a foundation for a monitoring and evaluation approach that is informed and grounded by practices worldwide to better support implementation.</p>
    <p><b>Whole School/System Trainings and Courses:</b> Utilizing theories for comprehensive school-wide and system-wide implementation to address the sustainability of HEART Learning and SEL programs.</p>
  </div>

  <div class="team-band"></div>
  <h2 class="team-title">Student Team</h2>
  <p class="team-note">Currently, over 38 undergraduates, masters students, and PhD students from Halden and globally have been a part of our student research team.</p>

  <div class="team-panel"></div>
  <div class="pill pill--green" style="top:428px;left:168px;width:222px;height:23px;font-family:'Poppins',sans-serif;font-weight:700;font-size:13px;line-height:23px">Student Team</div>
  <div class="pubs">
    <p>US: Marlow, J., Ashby, L., Kettner-Vale, P. (2024). Cultivating compassion in educational settings - evaluating the effectiveness of a compassion-based SEL program in elementary school children in the US. Open Science Letters. In review.</p>
    <p>Colombia: Marlow, J., Ortega Ruiz, C., Medina Salas, D., &amp; Pryce, H. (2024). Resilience and Renewal: Exploring the Role of Social, Emotional, and Ethical Learning in Elementary Schools in Colombia. Journal of Learning Studies. In review.</p>
    <p>South Korea: Seo, D. H., Han, J. W., Yoon, M. K., &amp; Baek, S. (2024). Building Resilience and Social–Emotional Competencies in Elementary School Students through a Short-Term Intervention Program Based on the HEART Learning Curriculum. Behavior &amp; Mind, 14(6), 458.</p>
    <p>Ukraine: Kovalenko, I., Sydorenko, O., &amp; Marlow, J. (2024). The Effects of a School-Based Social-Emotional and Ethical Learning Program on the Well-Being of Ukrainian Classrooms in the Context of War. Crisis &amp; Care. In Review</p>
    <p>Brazil: Ferreira, L., Almeida, R., Costa, V., &amp; Marlow, J. (2024). Mental health improvements of a four-week social, emotional and ethical learning training in Brazilian public school teachers. Horizons in Psychology, Educational Psychology. In review.</p>
    <p>Mongolia: Batbold, A., Tsogt, E., &amp; Marlow, J. (2024). Predicting the happiness and life satisfaction of middle school students by family factors. Studies in Schooling, 24(598), 598.</p>
    <p>Global Integration: Marlow, J., &amp; Dunmore, K. (2023). Nurturing positive mental health and wellbeing in educational settings – the BRIGHT model. Horizons in Public Health, 11.</p>
  </div>

  <svg class="footer-shape" viewBox="0 0 557 86" aria-hidden="true">
    <path d="M0 86 V65 H108 C142 65 146 7 182 7 L401 7 C437 7 441 65 475 65 H557 V86Z" fill="#fff"/>
  </svg>
  <div class="partner" style="left:178px;top:724px">
    <span class="brand-name" style="font-size:16px;line-height:20px">HEART Learning</span>
    <span class="badge" style="width:32px;height:36px;border-radius:4px;margin-left:12px;background:var(--blue)"></span>
  </div>
</section>

</body>
</html>
```